Harborline Motors LLC

Car Dealer Customer Service
Address: 2741 Linden Avenue, Shelbyville, TN 37162
web: www.harborlinemotorstn.net
email: harborlinemotorstn@mailbox-example.net
Phone: (931) 555-0148
Phone: (629) 555-0173

```html
<!DOCTYPE html>
<html lang="en">
<head>
<meta charset="utf-8">
<title>Harborline Motors – Business Card</title>
<link rel="stylesheet" href="https://fonts.googleapis.com/css2?family=Source+Sans+3:wght@400;600;700&display=swap">
<style>
  :root {
    --brand-blue: #1f78ad;
    --icon-blue: #2b93d1;
    --deep-blue: #0a76b1;
    --sun-yellow: #f3b02b;
    --panel-yellow: #ebb247;
    --cream: #fff3c2;
    --sky: #dfeaf6;
    --white: #ffffff;
    --page: #ffffff;
  }
  * { margin: 0; padding: 0; box-sizing: border-box; }
  html, body {
    width: 1200px; height: 900px; overflow: hidden;
    background: var(--page);
    font-family: "Source Sans 3", sans-serif;
  }
  .card {
    position: absolute; left: 285px; width: 630px; height: 360px; overflow: hidden;
  }
  .card--front {
    top: 63px;
    background:
      radial-gradient(ellipse 55% 60% at 50% 50%, rgba(255,255,255,0.95), rgba(255,255,255,0) 100%),
      linear-gradient(180deg, var(--deep-blue) 0%, #7fa6cc 25%, #b9a98a 55%, #f2c060 80%, var(--cream) 100%);
  }
  .card--front::after {
    content: ""; position: absolute; inset: 0;
    background:
      radial-gradient(ellipse 40% 35% at 50% 0%, rgba(223,234,246,0.9), rgba(223,234,246,0) 100%),
      radial-gradient(ellipse 40% 30% at 50% 100%, rgba(255,243,194,0.95), rgba(255,243,194,0) 100%),
      radial-gradient(circle at 0% 100%, var(--sun-yellow), rgba(243,176,43,0) 35%),
      radial-gradient(circle at 100% 100%, var(--sun-yellow), rgba(243,176,43,0) 35%);
  }
  .front-brand {
    position: absolute; inset: 0; z-index: 1;
    display: flex; flex-direction: column; align-items: center; justify-content: center; gap: 18px;
    padding-top: 20px;
  }
  .brand-dot { width: 90px; height: 90px; border-radius: 50%; background: var(--brand-blue); }
  .brand-name {
    font-weight: 700; color: var(--brand-blue); letter-spacing: 0.5px; white-space: nowrap;
  }
  .front-brand .brand-name { font-size: 32px; }

  .card--back { top: 477px; background: var(--white); }
  .back-panel { position: absolute; left: 0; top: 0; }
  .back-brand {
    position: absolute; left: 20px; width: 230px; top: 70px;
    display: flex; flex-direction: column; align-items: center;
  }
  .back-brand .brand-dot { width: 76px; height: 76px; margin-bottom: 22px; }
  .back-brand .brand-name { font-size: 21px; }
  .brand-tagline {
    color: var(--white); font-size: 12px; font-weight: 600; margin-top: 3px; white-space: nowrap;
  }
  .contact-list {
    position: absolute; right: 40px; top: 80px; list-style: none;
    display: flex; flex-direction: column; gap: 10px;
  }
  .contact-item {
    display: flex; align-items: center; justify-content: flex-end; gap: 16px;
    color: var(--brand-blue); font-weight: 600; font-size: 18px; line-height: 22px; text-align: right;
  }
  .contact-item--email { font-size: 14.5px; }
  .contact-item--address { align-items: flex-start; }
  .contact-icon {
    flex: none; width: 27px; height: 27px; border-radius: 5px; background: var(--icon-blue);
    display: flex; align-items: center; justify-content: center;
  }
  .contact-icon svg { width: 17px; height: 17px; }
</style>
</head>
<body>
  <section class="card card--front">
    <div class="front-brand">
      <div class="brand-dot"></div>
      <div class="brand-name">HARBORLINE MOTORS</div>
    </div>
  </section>

  <section class="card card--back">
    <svg class="back-panel" width="300" height="360" viewBox="0 0 300 360" aria-hidden="true">
      <path d="M0 0 H210 Q300 180 210 360 H0 Z" fill="var(--panel-yellow)"/>
    </svg>
    <div class="back-brand">
      <div class="brand-dot"></div>
      <div class="brand-name">HARBORLINE MOTORS</div>
      <div class="brand-tagline">CAR DEALER CUSTOMER SERVICE</div>
    </div>

    <ul class="contact-list">
      <li class="contact-item">
        <span>(931) 555-0148<br>(629) 555-0173</span>
        <span class="contact-icon"><svg viewBox="0 0 24 24"><path fill="#fff" d="M6.6 10.8a15 15 0 0 0 6.6 6.6l2.2-2.2c.3-.3.7-.4 1-.2 1.1.4 2.3.6 3.6.6.6 0 1 .4 1 1V20c0 .6-.4 1-1 1A17 17 0 0 1 3 4c0-.6.4-1 1-1h3.5c.6 0 1 .4 1 1 0 1.3.2 2.5.6 3.6.1.3 0 .7-.2 1z"/></svg></span>
      </li>
      <li class="contact-item contact-item--email">
        <span>harborlinemotorstn@mailbox-example.net</span>
        <span class="contact-icon"><svg viewBox="0 0 24 24" fill="none" stroke="#fff" stroke-width="2.2"><rect x="3" y="5" width="18" height="14"/><path d="M3 5l9 8 9-8"/></svg></span>
      </li>
      <li class="contact-item">
        <span>www.harborlinemotorstn.net</span>
        <span class="contact-icon"><svg viewBox="0 0 24 24" fill="none" stroke="#fff" stroke-width="2"><circle cx="12" cy="12" r="9"/><ellipse cx="12" cy="12" rx="4" ry="9"/><path d="M3 12h18"/></svg></span>
      </li>
      <li class="contact-item contact-item--address">
        <span>2741 Linden Avenue,<br>Shelbyville,<br>TN 37162</span>
        <span class="contact-icon"><svg viewBox="0 0 24 24"><path fill="#fff" d="M12 2a7 7 0 0 0-7 7c0 5 7 13 7 13s7-8 7-13a7 7 0 0 0-7-7zm0 9.5A2.5 2.5 0 1 1 12 6.5a2.5 2.5 0 0 1 0 5z"/></svg></span>
      </li>
    </ul>
  </section>
</body>
</html>
```